Business Card Design Project

- makeup artist business card

- original and creative

- Elegant design

- Feel free to come out with cool designs but stick to being elegant and attractive

- Design relates to makeup

- includes name, occupation, contact numbers, email, website

- regular size business card

- round corner card

- double sided

- on 1 side it should just have the website name in the center " browsandblush.example "

Industry/Entity Type

Business

Requirements
Must have
• Marla Voss
Makeup Artist
USA: +1 (415)872-6410
Singapore: +65 83027715
marlavoss@browsandblush.example
www.browsandblush.example
Should not have
• nothing cartoon looking.
Pictures of makeup being grab from the internet.. Examples: eyes or lips.

```html
<!DOCTYPE html>
<html lang="en">
<head>
<meta charset="utf-8">
<title>Marla Voss – Makeup Artist Business Card</title>
<link rel="stylesheet" href="https://fonts.googleapis.com/css2?family=Cinzel:wght@400;600&display=swap">
<style>
  :root {
    --backdrop: #2b2b2d;
    --rose-deep: #8c1a32;
    --rose-mid: #b54a62;
    --rose-light: #d98a9a;
    --gold-dark: #a9801f;
    --gold-mid: #e3c363;
    --gold-light: #f6e7a6;
    --ink: #1d1416;
    --paper-white: #f7eef0;
  }
  * { box-sizing: border-box; margin: 0; padding: 0; }
  html, body {
    width: 1200px;
    height: 890px;
    overflow: hidden;
    background: var(--backdrop);
  }
  .canvas {
    position: relative;
    width: 1200px;
    height: 890px;
  }
  .card {
    position: absolute;
    left: 320px;
    width: 560px;
    height: 320px;
    border-radius: 22px;
    overflow: hidden;
    background: radial-gradient(ellipse at 62% 20%, var(--rose-light) 0%, var(--rose-mid) 38%, var(--rose-deep) 100%);
    font-family: "Cinzel", serif;
    box-shadow: 0 14px 30px rgba(0, 0, 0, 0.45);
  }
  .card--front { top: 90px; }
  .card--back { top: 480px; }

  .eye-art {
    position: absolute;
    border-radius: 50%;
    background: radial-gradient(ellipse at center, rgba(240, 190, 185, 0.55) 0%, rgba(220, 150, 155, 0.3) 55%, rgba(181, 74, 98, 0) 100%);
  }
  .card--front .eye-art {
    left: 150px;
    top: 10px;
    width: 280px;
    height: 80px;
  }
  .card--back .eye-art {
    left: 150px;
    top: 40px;
    width: 260px;
    height: 120px;
  }

  .identity {
    position: absolute;
    left: 0;
    right: 0;
    top: 92px;
    text-align: center;
    color: var(--ink);
  }
  .identity__name {
    font-size: 40px;
    font-weight: 400;
    letter-spacing: 1px;
    line-height: 1;
  }
  .identity__role {
    margin-top: 2px;
    margin-left: 90px;
    font-size: 12px;
    font-weight: 600;
    letter-spacing: 1.5px;
    text-transform: uppercase;
  }

  .gold-band {
    position: absolute;
    left: 0;
    right: 0;
    top: 172px;
    height: 96px;
    background: linear-gradient(100deg, var(--gold-dark) 0%, var(--gold-mid) 30%, var(--gold-light) 55%, var(--gold-mid) 78%, var(--gold-dark) 100%);
    display: flex;
    flex-direction: column;
    justify-content: center;
    align-items: center;
    gap: 3px;
    color: var(--ink);
  }
  .contact-line {
    font-size: 14px;
    letter-spacing: 0.8px;
    text-transform: uppercase;
    line-height: 1.2;
  }

  .website {
    position: absolute;
    left: 0;
    right: 0;
    top: 186px;
    text-align: center;
    color: var(--paper-white);
    font-size: 30px;
    letter-spacing: 1.5px;
    text-transform: uppercase;
  }
</style>
</head>
<body>
  <main class="canvas">
    <section class="card card--front">
      <div class="eye-art" role="img" aria-label="Soft illustration of a pair of made-up eyes"></div>
      <div class="identity">
        <h1 class="identity__name">Marla Voss</h1>
        <p class="identity__role">Makeup Artist</p>
      </div>
      <div class="gold-band">
        <p class="contact-line">USA: +1 (415)872-6410</p>
        <p class="contact-line">Singapore: +65 83027715</p>
        <p class="contact-line">marlavoss@browsandblush.example</p>
      </div>
    </section>

    <section class="card card--back">
      <div class="eye-art" role="img" aria-label="Soft illustration of a single made-up eye"></div>
      <p class="website">www.browsandblush.example</p>
    </section>
  </main>
</body>
</html>
```